Book cover for LM

Design cover for a book of gratitude and inspiration.
Book trim size will be 6.5 x 6.5 inches, or 8 x 8 inches, hardcover, 96 pages
Title: Lantern Meadows
Subtitle: A Book of Gratitude and Inspiration
Author: Gus Halverd

```html
<!DOCTYPE html>
<html lang="en">
<head>
<meta charset="utf-8">
<title>Lantern Meadows — Book Cover</title>
<link rel="stylesheet" href="https://fonts.googleapis.com/css2?family=Cinzel+Decorative:wght@400;700&family=Josefin+Sans:wght@700&family=Marcellus&display=swap">
<style>
  :root {
    --sky-top: #c98283;
    --sky-rose: #e9a08a;
    --sun-core: #fffbe8;
    --sun-glow: #fde86a;
    --horizon: #e8602e;
    --hill: #221816;
    --meadow: #120e0c;
    --ink: #0d0a09;
    --author-red: #c4221a;
  }
  html, body {
    margin: 0;
    padding: 0;
    width: 1200px;
    height: 1200px;
    overflow: hidden;
    background: var(--meadow);
  }
  .cover {
    position: relative;
    width: 1200px;
    height: 1200px;
    overflow: hidden;
  }
  .cover-scene {
    position: absolute;
    inset: 0;
    background:
      radial-gradient(circle at 52% 47%, var(--sun-core) 0, #fff6c8 90px, var(--sun-glow) 180px, rgba(245,150,90,0.85) 300px, rgba(233,160,138,0) 470px),
      linear-gradient(to bottom, var(--sky-top) 0%, var(--sky-rose) 35%, var(--horizon) 53%, var(--hill) 58%, #2a1a16 68%, var(--meadow) 100%);
  }
  .title {
    position: absolute;
    left: 0;
    top: 0;
    margin: 0;
    font-family: "Cinzel Decorative", "Cinzel", serif;
    font-weight: 400;
    color: var(--ink);
    line-height: 1;
  }
  .title-line {
    position: absolute;
    white-space: nowrap;
  }
  .title-line--first {
    left: 92px;
    top: 140px;
    font-size: 168px;
    letter-spacing: -2px;
  }
  .title-line--second {
    left: 206px;
    top: 318px;
    font-size: 168px;
    letter-spacing: -4px;
  }
  .subtitle {
    position: absolute;
    left: 371px;
    top: 503px;
    width: 714px;
    margin: 0;
    font-family: "Josefin Sans", sans-serif;
    font-weight: 700;
    font-size: 29px;
    letter-spacing: 0.3px;
    text-align: justify;
    text-align-last: justify;
    color: var(--ink);
    white-space: nowrap;
  }
  .author {
    position: absolute;
    left: 376px;
    top: 1046px;
    margin: 0;
    font-family: "Marcellus", serif;
    font-size: 76px;
    letter-spacing: -1px;
    color: var(--author-red);
    white-space: nowrap;
  }
</style>
</head>
<body>
  <main class="cover">
    <div class="cover-scene" role="img" aria-label="Sunset over dark rolling hills, with a meadow of glowing red-orange flowers in the foreground"></div>
    <h1 class="title">
      <span class="title-line title-line--first">LANTERN</span>
      <span class="title-line title-line--second">MEADOWS</span>
    </h1>
    <p class="subtitle">A BOOK OF GRATITUDE AND INSPIRATION</p>
    <p class="author">GUS HALVERD</p>
  </main>
</body>
</html>
```